Email Signature Design (GIF)

I need an Email Signature designed, In a GIF format. The following Excel File and Logo Image should be applied. The Logo on the left and the Fixed "Supplying" and rotating words amongst the variety appears on the right.
e.g. "(VT LOGO) Supplying (Variant)" . Please us the Quorvix screenshots, only as an example.

Target Market(s)

Our current customer base (Construction)

Industry/Entity Type

Construction

Font styles to use
Sans Serif

Requirements
Must have
• My project Must follow the instructions in the Project description

```html
<!DOCTYPE html>
<html lang="en">
<head>
<meta charset="utf-8">
<title>VT Email Signature</title>
<link href="https://fonts.googleapis.com/css2?family=Poppins:wght@400;500&display=swap" rel="stylesheet">
<style>
  :root {
    --paper: #ffffff;
    --ink: #141414;
    --brand-navy: #2e1a87;
    --divider: #2c3b8e;
  }
  * { margin: 0; padding: 0; box-sizing: border-box; }
  html, body {
    width: 1200px;
    height: 500px;
    overflow: hidden;
    background: var(--paper);
  }
  .signature {
    position: relative;
    width: 1200px;
    height: 500px;
    background: var(--paper);
    font-family: "Poppins", sans-serif;
    color: var(--ink);
  }
  .brand {
    position: absolute;
    left: 67px;
    top: 67px;
    width: 361px;
    height: 311px;
    display: flex;
    align-items: center;
    justify-content: center;
    gap: 22px;
  }
  .brand-dot {
    width: 34px;
    height: 34px;
    border-radius: 50%;
    background: var(--brand-navy);
  }
  .brand-name {
    font-family: "Poppins", sans-serif;
    font-weight: 500;
    font-size: 120px;
    line-height: 1;
    color: var(--brand-navy);
  }
  .divider {
    position: absolute;
    left: 509px;
    top: 42px;
    width: 5px;
    height: 428px;
    background: var(--divider);
  }
  .tagline {
    position: absolute;
    left: 627px;
    top: 106px;
    font-weight: 500;
    font-size: 31px;
    letter-spacing: 5px;
    text-transform: uppercase;
  }
  .contact {
    position: absolute;
    left: 628px;
    top: 366px;
    list-style: none;
    font-weight: 500;
    font-size: 21px;
    line-height: 27px;
    text-transform: uppercase;
  }
  .contact-item {
    display: flex;
    align-items: flex-start;
    gap: 14px;
  }
  .contact-item + .contact-item { margin-top: 14px; }
  .contact-icon {
    flex: none;
    width: 22px;
    height: 27px;
    fill: var(--ink);
  }
</style>
</head>
<body>
  <main class="signature">
    <div class="brand">
      <span class="brand-dot"></span>
      <span class="brand-name">VT</span>
    </div>

    <div class="divider"></div>

    <p class="tagline">Supplying</p>

    <ul class="contact">
      <li class="contact-item">
        <svg class="contact-icon" viewBox="0 0 22 27" aria-hidden="true">
          <path d="M3 10c0-2 1-3 3-3.4C8.5 6 13.5 6 16 6.6 18 7 19 8 19 10l-3.6.6-.6-2.3H7.2l-.6 2.3z"/>
          <path d="M6.5 11.5h9l3 5v4.5h-15v-4.5z"/>
          <circle cx="11" cy="16.3" r="2" fill="#fff"/>
        </svg>
        <span>(02) 5550 4186</span>
      </li>
      <li class="contact-item">
        <svg class="contact-icon" viewBox="0 0 22 27" aria-hidden="true">
          <path d="M11 2C6.6 2 3 5.5 3 9.9 3 15.5 11 24 11 24s8-8.5 8-14.1C19 5.5 15.4 2 11 2zm0 11a3.2 3.2 0 1 1 0-6.4 3.2 3.2 0 0 1 0 6.4z"/>
        </svg>
        <span>27 Marlowe Street | Brindale, NSW 2147<br>PO Box 4420 | Kellswood NSW 2131</span>
      </li>
    </ul>
  </main>
</body>
</html>
```